Harborline Bridal Bakery Selling Method needs finishing touches to website.

We have a temporary website located at http://www.brivantomarketworks.com/ql/.
We are doing a responsive design and have created the architecture (layout). However, we need a professional makeover for the graphic elements and colors of the website. The website will be selling a sales course to mostly women who sell wedding cakes.
The photos within the posted website are for illustrative purposes. We will use our own photos after the website is redone.
We are open to changing the font styles, borders, header, and anything else as long as the layout is not changed.
Target Market(s)
75% women age 25-50 and men 30-60.
Industry/Entity Type
Architecture
Colors
Designer to choose colors to be used in the design.
Look and feel
Each slider illustrates characteristics of the customer's brand and the style your logo design should communicate.

```html
<!DOCTYPE html>
<html lang="en">
<head>
<meta charset="utf-8">
<title>Harborline Bridal Bakery Selling Method</title>
<link rel="stylesheet" href="https://fonts.googleapis.com/css2?family=Alegreya:wght@400;700&family=Merriweather:wght@400&family=Open+Sans:ital,wght@0,400;0,600;0,700;1,400&display=swap">
<style>
  :root {
    --peach: #f6dccc;
    --paper: #f3efea;
    --rose: #c8506a;
    --rose-dark: #a83a53;
    --charcoal: #3a3a3a;
    --ink: #333333;
    --white: #ffffff;
    --line: #555555;
  }
  * { box-sizing: border-box; margin: 0; padding: 0; }
  html, body { width: 1100px; height: 1200px; overflow: hidden; }
  body {
    background: var(--peach);
    font-family: "Open Sans", Arial, sans-serif;
    color: var(--ink);
    position: relative;
  }
  .page {
    position: absolute; left: 144px; top: 0; width: 812px; height: 1200px;
    background: var(--paper);
  }
  .abs { position: absolute; }

  .site-title {
    left: 154px; top: 10px; width: 792px; height: 69px;
    background: var(--rose);
    box-shadow: 0 3px 4px rgba(0,0,0,.18);
    color: var(--white);
    font-family: "Alegreya", Georgia, serif; font-weight: 400;
    font-size: 29px; line-height: 69px; text-align: center;
    white-space: nowrap; overflow: hidden;
  }
  .site-title strong { font-weight: 700; }

  .main-nav {
    left: 172px; top: 93px; width: 752px; height: 41px;
    border-top: 3px double var(--line); border-bottom: 3px double var(--line);
    display: flex; align-items: center; justify-content: space-between;
    padding: 0 8px;
    font-family: "Merriweather", Georgia, serif; font-size: 15px; color: #444;
    white-space: nowrap;
  }
  .main-nav .nav-items { display: flex; gap: 58px; margin-left: 20px; }
  .main-nav .active { color: var(--rose); }
  .main-nav .diamond { font-size: 11px; }

  .hero-video {
    left: 154px; top: 151px; width: 533px; height: 352px;
    background: linear-gradient(160deg, #e7d3bf 0%, #c9a684 45%, #8c5d3c 100%);
  }
  .play-btn { left: 377px; top: 273px; }

  .signup {
    left: 687px; top: 151px; width: 259px; height: 352px;
    background: var(--charcoal); color: var(--white); text-align: center;
  }
  .signup h2 { margin-top: 4px; font-weight: 700; font-size: 24px; white-space: nowrap; }
  .signup p.lead { font-size: 16px; line-height: 20px; margin-top: 4px; padding: 0 38px; }
  .signup .arrow { display: block; margin: 6px auto 0; }
  .signup .field {
    display: block; width: 233px; height: 39px; margin: 12px auto 0;
    background: var(--white); border-radius: 9px; color: #555;
    font-size: 14px; line-height: 39px; text-align: left; padding-left: 17px;
  }
  .signup .cta {
    display: block; width: 224px; height: 44px; margin: 18px auto 0;
    background: var(--rose); border-radius: 8px; border: 2px solid var(--rose-dark);
    color: var(--white); font-weight: 700; font-size: 20px; line-height: 40px;
  }
  .signup .note { font-size: 13px; margin-top: 11px; }

  .section-ribbon {
    left: 135px; top: 533px; width: 830px; height: 70px;
    background: var(--charcoal); color: var(--white);
    font-family: "Alegreya", Georgia, serif; font-weight: 400; font-size: 29px;
    line-height: 70px; text-align: center; white-space: nowrap;
    box-shadow: 0 3px 5px rgba(0,0,0,.25);
  }
  .ribbon-fold { top: 603px; }

  .card {
    top: 611px; width: 246px; height: 330px;
    background: var(--white); box-shadow: 0 1px 3px rgba(0,0,0,.2);
  }
  .card .photo { position: absolute; left: 6px; top: 6px; width: 234px; height: 172px; }
  .card .caption {
    position: absolute; left: 6px; top: 178px; width: 234px; height: 64px;
    background: var(--charcoal); color: var(--white);
    font-size: 11px; font-style: italic; line-height: 14px;
    text-align: center; padding: 9px 12px 0;
  }
  .card .caption.featured { background: var(--rose); }
  .card .excerpt {
    position: absolute; left: 8px; top: 250px; width: 228px;
    font-size: 12px; line-height: 17px; color: var(--ink);
  }
  .card .excerpt.centered { text-align: center; }
  .read-more {
    position: absolute; top: 320px; left: 62px; width: 102px; height: 20px;
    background: var(--charcoal); color: var(--white);
    font-size: 11.5px; font-weight: 600; line-height: 20px; text-align: center;
    clip-path: polygon(8% 0, 92% 0, 100% 50%, 92% 100%, 8% 100%, 0 50%);
  }

  .seen-title {
    left: 158px; top: 990px; width: 786px; height: 20px;
    border-top: 3px double #bbb;
    font-style: italic; font-weight: 600;
    font-size: 17px; color: var(--ink); text-align: center;
  }
  .seen-title span { position: relative; top: -13px; background: var(--paper); padding: 0 6px; }
  .press-strip {
    left: 154px; top: 1024px; width: 784px; height: 65px;
    background: var(--white); box-shadow: 0 1px 3px rgba(0,0,0,.2);
    display: flex; align-items: center; justify-content: space-around; padding: 0 20px;
  }
  .press-badge { background: #c8c8c8; }

  .site-footer {
    left: 144px; top: 1104px; width: 812px; height: 96px;
    background: var(--charcoal); border-top: 4px solid var(--rose); color: var(--white);
  }
  .site-footer .copy { position: absolute; left: 14px; top: 34px; font-size: 11.5px; }
  .site-footer .links { position: absolute; left: 14px; top: 53px; font-size: 11.5px; }
  .site-footer .links span { margin: 0 9px; }
  .site-footer .social { position: absolute; left: 680px; top: 28px; font-size: 13px; font-weight: 600; }
  .site-footer .dots { display: flex; gap: 3px; margin-top: 10px; margin-left: 4px; }
  .site-footer .dots i { display: block; width: 20px; height: 20px; border-radius: 50%; background: #e6e6e6; }
  .site-footer .dots i:first-child { background: var(--rose); }
</style>
</head>
<body>
<div class="page"></div>

<header class="abs site-title">Cracking The <strong>"Secret Code"</strong> That Unlocks Your Wedding Cake Sales!</header>

<nav class="abs main-nav">
  <span class="diamond">&#10070;</span>
  <div class="nav-items">
    <span class="active">Home</span>
    <span>Who Is Lou Brannick</span>
    <span>Why Lou Is Sharing His Secrets</span>
    <span>Contact</span>
  </div>
  <span class="diamond">&#10070;</span>
</nav>

<div class="abs hero-video" role="img" aria-label="Smiling baker holding a wrapped cake in a bakery shop"></div>
<svg class="abs play-btn" width="110" height="110" viewBox="0 0 110 110" aria-hidden="true">
  <circle cx="55" cy="55" r="50" fill="rgba(255,255,255,.15)" stroke="#444" stroke-width="5"/>
  <polygon points="44,30 44,80 82,55" fill="#444"/>
</svg>

<aside class="abs signup">
  <h2>FREE VIDEOS TO HELP</h2>
  <p class="lead">You Sell More Wedding Cakes At Higher Prices... Immediately</p>
  <svg class="arrow" width="60" height="40" viewBox="0 0 60 40" aria-hidden="true">
    <polygon points="18,0 42,0 42,14 58,14 30,40 2,14 18,14" fill="var(--rose)"/>
  </svg>
  <span class="field">Your Name</span>
  <span class="field">Your Email</span>
  <span class="cta">Get Instant Access</span>
  <p class="note">No Spam. I Promise.</p>
</aside>

<h2 class="abs section-ribbon">3 Leading-Edge Techniques for Convincing Brides to Choose You</h2>
<svg class="abs ribbon-fold" style="left:135px" width="10" height="10" aria-hidden="true"><polygon points="0,0 10,0 10,10" fill="#222"/></svg>
<svg class="abs ribbon-fold" style="left:955px" width="10" height="10" aria-hidden="true"><polygon points="0,0 10,0 0,10" fill="#222"/></svg>

<article class="abs card" style="left:154px">
  <div class="photo" role="img" aria-label="Baker behind a counter of breads and cakes" style="background:linear-gradient(160deg,#c79a5e,#6e4a2c)"></div>
  <p class="caption featured">In the first video, discover a sales growth secret that reveals the "Two Faces Of Your Wedding Cake Business."</p>
  <p class="excerpt">One side of your face displays your "Internal Reality." It's how you run your business. Whether...</p>
  <span class="read-more">Read More</span>
</article>

<article class="abs card" style="left:423px">
  <div class="photo" role="img" aria-label="Baker presenting a tray of pastries" style="background:linear-gradient(160deg,#2a2a2a,#a58f7c)"></div>
  <p class="caption">In the second video you'll peek at my most effective psychological sales secret called "The Insecurity Gap."</p>
  <p class="excerpt centered">The #1 Reason You're Not Selling More Wedding Cakes...is due to "The Insecurity Gap" a bride...</p>
  <span class="read-more">Read More</span>
</article>

<article class="abs card" style="left:692px">
  <div class="photo" role="img" aria-label="Customer receiving a wrapped cake at a market stall" style="background:linear-gradient(160deg,#e8ddd2,#b68e6a)"></div>
  <p class="caption">In the third video, you will find out how to use Your "External Perception to WIN more wedding cake orders.</p>
  <p class="excerpt">Start thinking in terms of being the "World's Greatest"... not Chicago's best...</p>
  <span class="read-more">Read More</span>
</article>

<svg class="abs" style="left:541px;top:969px" width="20" height="21" viewBox="0 0 20 21" aria-hidden="true">
  <rect x="5" y="0" width="10" height="6" fill="var(--rose)"/>
  <rect x="2" y="7" width="16" height="6" fill="var(--rose)"/>
  <rect x="0" y="14" width="20" height="7" fill="var(--rose)"/>
</svg>
<div class="abs seen-title"><span>Lou Brannick as seen:</span></div>

<div class="abs press-strip">
  <div class="press-badge" style="width:36px;height:36px"></div>
  <div class="press-badge" style="width:118px;height:24px"></div>
  <div class="press-badge" style="width:36px;height:36px;border-radius:50%"></div>
  <div class="press-badge" style="width:42px;height:36px"></div>
  <div class="press-badge" style="width:92px;height:36px"></div>
  <div class="press-badge" style="width:80px;height:30px"></div>
</div>

<footer class="abs site-footer">
  <p class="copy">Copyright © 2014 The Frosting Parlor. Phone: 555.014.2290. All Rights Reserved.</p>
  <p class="links">Home<span>|</span>Who Is Lou Brannick<span>|</span>Why Lou Is Sharing His Secrets<span>|</span>Contact</p>
  <div class="social">Connect with us
    <div class="dots"><i></i><i></i><i></i></div>
  </div>
</footer>
</body>
</html>
```